Tarn - Stationary Design/Layout

We are a well established clothing design and manufacturing company (Tarn Sourcing) based in London UK, with our own factory in Bangladesh, supplying to many fashion retailers and brands. Our factory has very high environmental and ethical standards with people at its heart. Our quality of garments are second to none.
Our new logo has been proudly developed by the Pixel Guild community last month, we are now in the second phase and need the layout designed for our letterheads, double sided business cards, compliment slip and clothing ticket. Feel as creative as you like, but make sure it looks great!!
***The Logo - the logo design and colour is set and should NOT be changed and stay on a dark grey backround. The logo artwork to use is attached.
***Details to use for the business card:
Dorian Pelham
Direct Line: 020 7946 0158
dorian@tarnsourcing-example.com
Tarn Sourching Ltd.
57 - 59 Hollin Row
Harlowe . Brindmoor
NW9 4QT
Switchboard: 020 7946 0274
Fax: 020 7946 0274
www.tarnsourcing-example.co.uk
***Details to use for the letterhead and compliment slip:
Tarn Sourching Ltd.
57 - 59 Hollin Row
Harlowe . Brindmoor
NW9 4QT
Fax: 020 7946 0274
www.tarnsourcing-example.co.uk
***Details for Swing Ticket:
Size: 12cm height by 5.5cm width
One side need to have just the logo without the 'Sourcing', on the other it needs to stay blank

```html
<!DOCTYPE html>
<html lang="en">
<head>
<meta charset="utf-8">
<title>Tarn Sourcing – Business Card</title>
<link href="https://fonts.googleapis.com/css2?family=Source+Sans+3:wght@400;600;700&display=swap" rel="stylesheet">
<style>
  :root {
    --backdrop: #e9e5e1;
    --card-dark: #3c3c3c;
    --card-light: #ffffff;
    --ink: #4a4a4a;
    --ink-strong: #3a3a3a;
    --brand-blue: #a9dde5;
    --white: #ffffff;
  }
  * { margin: 0; padding: 0; box-sizing: border-box; }
  html, body {
    width: 1200px; height: 900px; overflow: hidden;
    background: var(--backdrop);
    font-family: "Source Sans 3", "Myriad Pro", sans-serif;
  }
  .canvas { position: relative; width: 1200px; height: 900px; }

  .card {
    position: absolute; top: 286px;
    width: 562px; height: 320px;
    border-radius: 14px; overflow: hidden;
    background: var(--card-dark);
    box-shadow: 0 2px 6px rgba(0,0,0,0.18);
  }
  .card--front { left: 15px; }
  .card--back { left: 623px; }

  .card__details {
    position: absolute; left: 0; top: 0; bottom: 0;
    width: 246px; background: var(--card-light);
    padding: 43px 0 0 39px; color: var(--ink);
    font-size: 13.6px; line-height: 18.6px;
    white-space: nowrap;
  }
  .card__name {
    font-size: 18px; font-weight: 700; color: var(--ink-strong);
    margin-bottom: 17px; line-height: 22px;
  }
  .card__group { margin-bottom: 18.6px; }

  .brand {
    position: absolute; white-space: nowrap; text-align: right;
    line-height: 1;
  }
  .brand__name {
    display: block; color: var(--brand-blue);
    font-weight: 600; letter-spacing: 0.04em;
  }
  .brand__sub { display: block; color: var(--white); letter-spacing: 0.01em; }

  .card--front .brand { right: 36px; top: 122px; }
  .card--front .brand__name { font-size: 62px; }
  .card--front .brand__sub { font-size: 17px; font-weight: 400; margin-top: 2px; }

  .card--back .brand { left: 50%; transform: translateX(-50%); top: 114px; }
  .card--back .brand__name { font-size: 86px; }
  .card--back .brand__sub { font-size: 22px; font-weight: 700; margin-top: 2px; }

  .card__web {
    position: absolute; left: 0; right: 0; top: 296px;
    text-align: center; color: var(--white);
    font-size: 13.5px; letter-spacing: 0.2em;
  }
  .card__web strong { font-weight: 700; }
</style>
</head>
<body>
<main class="canvas">
  <section class="card card--front" aria-label="Business card front">
    <div class="card__details">
      <p class="card__name">Dorian Pelham</p>
      <div class="card__group">
        <p>Direct Line: 020 7946 0158</p>
        <p>dorian@tarnsourcing-example.com</p>
      </div>
      <div class="card__group">
        <p>Tarn Sourching Ltd.</p>
        <p>57 - 59 Hollin Row</p>
        <p>Harlowe . Brindmoor</p>
        <p>NW9 4QT</p>
      </div>
      <div class="card__group">
        <p>Switchboard: 020 7946 0274</p>
        <p>Fax: 020 7946 0274</p>
        <p>www.tarnsourcing-example.co.uk</p>
      </div>
    </div>
    <div class="brand">
      <span class="brand__name">TARN</span>
      <span class="brand__sub">SOURCING</span>
    </div>
  </section>

  <section class="card card--back" aria-label="Business card back">
    <div class="brand">
      <span class="brand__name">TARN</span>
      <span class="brand__sub">SOURCING</span>
    </div>
    <p class="card__web">www.<strong>tarnsourcing-example</strong>.co.uk</p>
  </section>
</main>
</body>
</html>
```